Website design for recruitment solutions

We connect top talents to fast growing employers in Asia. We need to revamp our existing website (currently outdated) and also add more pages to make it more informative for talents and employers.
We need final design output to be for both desktop and mobile devices. The final design output must come with all specifications so it's easier for our dev team to implement. We have a detailed mockup but we expect the design to be significantly changed by the final output. We want the pages to look aesthetic, modern and professional.
Number of Pages Required
5+ page
Requirements
Must have
- - To have Pages design for desktop+mobile. Need to take into account intermediate resolutions like 1365px\1023px\767px\479px, especially if mobile/desktop design differs considerably. Design should be repeatable (between pages), suitable for block-layout.
Nice to have
- In terms of receiving files, we usually work with designers who can deliver files in Figma or Sketch with export to Figma. If in PSD format - please export to Zeplin or Avocode, otherwise will be difficult to open

```html
<!DOCTYPE html>
<html lang="en">
<head>
<meta charset="utf-8">
<title>HIRENEST – Recruitment</title>
<link href="https://fonts.googleapis.com/css2?family=Arimo:ital,wght@0,400;0,700;1,400&display=swap" rel="stylesheet">
<style>
:root{
  --red:#ef0f0f;
  --navy:#526f9a;
  --heading-blue:#4f6e9a;
  --ink:#222;
  --muted:#666;
  --grey-band:#e3e3e3;
  --white:#fff;
  --dark-btn:#2a2a2a;
}
*{margin:0;padding:0;box-sizing:border-box}
html,body{width:1200px;height:2860px;overflow:hidden;background:var(--white)}
body{position:relative;font-family:"Arimo",Arial,sans-serif;color:var(--ink)}
.abs{position:absolute}

/* hero */
.hero{left:0;top:0;width:1200px;height:640px;overflow:hidden}
.hero-photo{position:absolute;inset:0;background:linear-gradient(100deg,#6f7b88 0%,#a9a39b 30%,#b8b3ad 50%,#4d7fb0 70%,#5d6f82 100%)}
.hero-shade{position:absolute;inset:0;background:linear-gradient(180deg,rgba(0,0,0,.35),rgba(0,0,0,.05) 40%,rgba(0,0,0,.15))}
.hero-curve{position:absolute;left:0;top:0}
.logo{font-size:34px;font-weight:400;color:var(--white);letter-spacing:1px}
.site-logo{left:125px;top:30px}
.nav{top:42px;display:flex;gap:32px;left:383px}
.nav a{color:var(--white);text-decoration:none;font-size:15px}
.btn{display:inline-block;text-decoration:none;font-weight:700;color:var(--white);text-align:center}
.btn-red{background:var(--red)}
.btn-register{left:889px;top:28px;width:110px;height:42px;line-height:42px;font-size:18px}
.btn-login{left:1018px;top:28px;width:98px;height:42px;line-height:42px;font-size:18px;background:var(--dark-btn)}
.hero-title{left:0;width:1200px;top:212px;text-align:center;color:var(--white);font-size:44px;font-weight:700;line-height:56px;text-shadow:0 2px 6px rgba(0,0,0,.5)}
.btn-start{left:528px;top:343px;width:154px;height:48px;line-height:48px;font-size:19px}
.btn-start svg{vertical-align:-3px;margin-left:10px}
.learn-more{left:0;width:1200px;top:524px;text-align:center;color:var(--white);font-size:18px;text-shadow:0 1px 3px rgba(0,0,0,.6)}
.learn-icon{left:585px;top:561px}

/* features */
.feature-img{width:418px;height:312px}
.feature-img .photo{position:absolute;left:0;top:0;width:418px;height:312px;border:1px solid #ccc}
.feature-img .frame{position:absolute;left:9px;top:9px;width:418px;height:312px;background:var(--navy)}
.img-network{left:102px;top:714px}
.img-network .photo{background:radial-gradient(circle at 55% 40%,#6b6f78,#3b3f48 60%,#8a8f98)}
.img-meeting{left:671px;top:1140px}
.img-meeting .photo{background:linear-gradient(120deg,#d9d6cf,#b7aea3 40%,#7d6a5c 70%,#a0643f)}
.feature-title{font-size:40px;font-weight:700;color:var(--ink)}
.feature-text{font-size:16px;line-height:36px;color:#333}
.smart-title{left:595px;top:724px}
.smart-text{left:595px;top:780px;width:480px}
.insight-title{left:128px;top:1178px}
.insight-text{left:128px;top:1231px;width:462px;text-align:justify}

/* people first */
.people-band{left:0;top:1548px;width:1200px;height:268px;background:var(--grey-band)}
.section-title{left:0;width:1200px;text-align:center;font-size:40px;font-weight:700;color:var(--heading-blue)}
.people-title{top:1602px}
.people-text{left:0;width:1200px;top:1674px;text-align:center;font-size:17px;line-height:36px;color:#333}

/* testimonials */
.testi-title{top:1908px}
.avatar{left:559px;top:1985px;width:82px;height:82px;border-radius:50%;background:linear-gradient(180deg,#cfd3d6,#8a8f93);border:2px solid #ddd}
.quote-text{left:180px;width:840px;top:2082px;text-align:center;font-size:19px;line-height:40px;color:#777}
.arrow-btn{width:48px;height:48px}
.arrow-left{left:97px;top:2096px}
.arrow-right{left:1057px;top:2096px}
.quote-open{left:174px;top:2040px}
.quote-close{left:952px;top:2168px}
.person-name{left:0;width:1200px;top:2233px;text-align:center;font-size:21px;font-weight:700}
.person-role{left:0;width:1200px;top:2268px;text-align:center;font-size:21px;font-style:italic;color:#777}
.dots{left:568px;top:2309px;display:flex;gap:10px}
.dots span{width:14px;height:12px;background:#ccc}
.dots span.active{background:var(--white);border:1px solid #bbb}

/* footer */
.footer-curve{left:0;top:2360px}
.footer-logo{left:110px;top:2479px;font-size:26px}
.footer-about{left:111px;top:2528px;width:330px;font-size:15px;line-height:30px;color:var(--white)}
.footer-divider{left:453px;top:2470px;width:1px;height:214px;background:rgba(255,255,255,.45)}
.footer-col{top:2482px;color:var(--white)}
.footer-col h4{font-size:19px;font-weight:400;margin-bottom:22px}
.footer-col a{display:block;color:var(--white);text-decoration:none;font-size:16px;line-height:35px}
.col-talents{left:500px}
.col-employers{left:702px}
.col-about{left:911px}
.btn-footer-register{left:499px;top:2633px;width:110px;height:40px;line-height:40px;font-size:18px}
.social{left:107px;top:2691px;display:flex;gap:6px}
.social span{width:28px;height:28px;border-radius:50%;background:#e6ebf2}
.legal{top:2756px;font-size:13px;line-height:26px;color:var(--white)}
.legal-rights{left:111px;font-weight:700}
.legal-hk{left:420px}
.legal-sg{left:852px}
</style>
</head>
<body>

<header class="abs hero">
  <div class="hero-photo" role="img" aria-label="Photo of two professionals shaking hands across an office desk"></div>
  <div class="hero-shade"></div>
  <svg class="hero-curve" width="1200" height="640" viewBox="0 0 1200 640">
    <path d="M0 550 Q600 686 1200 550 L1200 640 L0 640 Z" fill="var(--red)"/>
    <path d="M0 552 Q600 710 1200 552 L1200 640 L0 640 Z" fill="#fff"/>
  </svg>
  <div class="abs logo site-logo">HIRENEST</div>
  <nav class="abs nav">
    <a href="#">HOW WE WORK</a><a href="#">BROWSE JOBS</a><a href="#">EMPLOYERS</a><a href="#">ABOUT US</a>
  </nav>
  <a class="abs btn btn-red btn-register" href="#">Register</a>
  <a class="abs btn btn-login" href="#">Log In</a>
  <h1 class="abs hero-title">We connect top talents into<br>fast growing employers in Asia</h1>
  <a class="abs btn btn-red btn-start" href="#">Get Started<svg width="10" height="16" viewBox="0 0 10 16"><path d="M2 1l6 7-6 7" stroke="#fff" stroke-width="2" fill="none"/></svg></a>
  <div class="abs learn-more">Learn More</div>
  <svg class="abs learn-icon" width="30" height="30" viewBox="0 0 30 30"><circle cx="15" cy="15" r="13" stroke="#fff" stroke-width="1.5" fill="none"/><path d="M10 13l5 5 5-5" stroke="#fff" stroke-width="1.5" fill="none"/></svg>
</header>

<section>
  <div class="abs feature-img img-network">
    <div class="frame"></div>
    <div class="photo" role="img" aria-label="Photo of a businessman touching a glowing network of connected people icons"></div>
  </div>
  <h2 class="abs feature-title smart-title">Smart Connections</h2>
  <p class="abs feature-text smart-text">It's the quality of the connection that matters. Our role matching algorithms and talent managers work around the<br>clock to find opportunities suitable to your unique profile.</p>

  <h2 class="abs feature-title insight-title">Critical insights</h2>
  <p class="abs feature-text insight-text">Our close interactions with candidates and employers have helped us create a comprehensive database ofcompanies, talents and skills. With HIRENEST, you will gain full access to timely intel to help you make the rightcareer decision.</p>
  <div class="abs feature-img img-meeting">
    <div class="frame"></div>
    <div class="photo" role="img" aria-label="Photo of two colleagues talking on a sofa in a bright modern lounge"></div>
  </div>
</section>

<section>
  <div class="abs people-band"></div>
  <h2 class="abs section-title people-title">People First</h2>
  <p class="abs people-text">We take the time to really understand you holistically as a person to maximize your potential. As your career<br>counselor, we provide maximum transparency and feedback throughout the process.</p>
</section>

<section>
  <h2 class="abs section-title testi-title">Testimonials</h2>
  <div class="abs avatar" role="img" aria-label="Portrait photo of the reviewer"></div>
  <svg class="abs quote-open" width="42" height="30" viewBox="0 0 42 30"><path d="M2 30V16Q2 4 16 0v6Q9 9 9 15h7v15ZM24 30V16Q24 4 38 0v6Q31 9 31 15h7v15Z" fill="#222"/></svg>
  <svg class="abs quote-close" width="42" height="30" viewBox="0 0 42 30"><path d="M40 0v14Q40 26 26 30v-6Q33 21 33 15h-7V0ZM18 0v14Q18 26 4 30v-6Q11 21 11 15H4V0Z" fill="#222"/></svg>
  <svg class="abs arrow-btn arrow-left" viewBox="0 0 48 48"><circle cx="24" cy="24" r="22" fill="#fff" stroke="#ddd" stroke-width="2"/><path d="M32 24H16M22 18l-6 6 6 6" stroke="#555" stroke-width="2" fill="none"/></svg>
  <svg class="abs arrow-btn arrow-right" viewBox="0 0 48 48"><circle cx="24" cy="24" r="22" fill="#fff" stroke="#ddd" stroke-width="2"/><path d="M16 24h16M26 18l6 6-6 6" stroke="#555" stroke-width="2" fill="none"/></svg>
  <p class="abs quote-text">Sed ut perspiciatis unde omnis iste natus error sit voluptatem accusantium doloremque laudantium, totam rem aperiam, eaque ipsa quae ab illo inventore veritatis et quasi architecto beatae vitae dicta sunt explicabo.</p>
  <div class="abs person-name">R.Marsh</div>
  <div class="abs person-role">Trader</div>
  <div class="abs dots"><span class="active"></span><span></span><span></span></div>
</section>

<footer>
  <svg class="abs footer-curve" width="1200" height="500" viewBox="0 2360 1200 500">
    <path d="M0 2450 Q600 2290 1200 2450 L1200 2860 L0 2860 Z" fill="var(--red)"/>
    <path d="M0 2452 Q600 2312 1200 2452 L1200 2860 L0 2860 Z" fill="var(--navy)"/>
  </svg>
  <div class="abs logo footer-logo">HIRENEST</div>
  <p class="abs footer-about">HIRENEST is a modern recruitment partner for high potential technology and talents. We work closely with hedge funds,systematic trading and FinTech employers experiencing hyper growth in Asia</p>
  <div class="abs footer-divider"></div>
  <div class="abs footer-col col-talents"><h4>TALENTS</h4><a href="#">How we work</a><a href="#">Browse jobs</a></div>
  <div class="abs footer-col col-employers"><h4>EMPLOYERS</h4><a href="#">Why HIRENEST</a></div>
  <div class="abs footer-col col-about"><h4>About Us</h4><a href="#">About HIRENEST</a><a href="#">Working at HIRENEST</a></div>
  <a class="abs btn btn-red btn-footer-register" href="#">Register</a>
  <div class="abs social"><span></span><span></span></div>
  <div class="abs legal legal-rights">HIRENEST&nbsp; 2012-2020 All rights reserved</div>
  <div class="abs legal legal-hk">Northgate Talent Limited(EA License No.40217)<br>Suite 12, Level 5, Harbourview Tower, 88 Seaview Road<br>Kowloon,Hong</div>
  <div class="abs legal legal-sg">Hirenest pte.Ltd.(License No.19C4406)<br>42 Marina Crest Rd,#14-02-Bayline Centre,<br>Singapore 018937</div>
</footer>

</body>
</html>
```